Candle company needs a label for candle

Looking for a designer to create my candle label. I am going to attach a few pictures of my vision for the label as well as my Company Logo and jar I have puchased. I'm going for the modern rustic feel but you are the designer and have full trust in your abilities. The label is going to be printed on Kraft paper (2x3) so looking for the font to be black. The candle label MUST include the following information:
Candle Birchway Co.
NO. 01: Eucalyptus + Spearmint
Handmade In NJ
Soy Wax
9oz

Industry/Entity Type

Candle Industry

Colors

Designer to choose colors to be used in the design.

Requirements
Should not have
• Any images

```html
<!DOCTYPE html>
<html lang="en">
<head>
<meta charset="UTF-8">
<title>Candle Birchway Co. — No. 01 Label</title>
<link href="https://fonts.googleapis.com/css2?family=Arvo:wght@400;700&display=swap" rel="stylesheet">
<style>
  :root {
    --page: #ffffff;
    --kraft: #c9a675;
    --kraft-edge: #bf9b69;
    --ink: #141210;
  }
  * { margin: 0; padding: 0; box-sizing: border-box; }
  html, body {
    width: 1200px;
    height: 1200px;
    overflow: hidden;
    background: var(--page);
  }
  .canvas {
    position: relative;
    width: 1200px;
    height: 1200px;
  }
  .label {
    position: absolute;
    left: 120px;
    top: 236px;
    width: 960px;
    height: 728px;
    background: var(--kraft);
    border: 1px solid var(--kraft-edge);
    border-radius: 30px;
    color: var(--ink);
    font-family: "Arvo", Georgia, serif;
  }
  .brand-name {
    position: absolute;
    left: 0;
    right: 0;
    top: 138px;
    text-align: center;
    font-size: 36px;
    font-weight: 400;
    line-height: 1.2;
  }
  .scent {
    position: absolute;
    left: 86px;
    top: 343px;
    font-size: 50px;
    font-weight: 700;
    line-height: 79px;
    letter-spacing: -0.01em;
    text-transform: uppercase;
    white-space: nowrap;
  }
  .details {
    position: absolute;
    left: 0;
    right: 0;
    top: 551px;
    text-align: center;
    font-size: 26px;
    font-weight: 700;
    line-height: 41px;
  }
  .weight-row {
    position: absolute;
    left: 108px;
    right: 100px;
    top: 652px;
    height: 40px;
    display: flex;
    align-items: center;
    gap: 34px;
    font-size: 27px;
    font-weight: 700;
  }
  .weight-row .rule {
    flex: 1;
    height: 2px;
    background: var(--ink);
  }
</style>
</head>
<body>
  <div class="canvas">
    <div class="label">
      <p class="brand-name">Candle Birchway Co.</p>
      <h1 class="scent">No. 01:<br>Eucalyptus + Spearmint</h1>
      <p class="details">Soy Wax<br>Handmade In NJ</p>
      <div class="weight-row">
        <span class="rule"></span>
        <span class="weight">9 oz</span>
        <span class="rule"></span>
      </div>
    </div>
  </div>
</body>
</html>
```